(주)케이비랩 라벨+박스 디자인 의뢰 사례 — 라벨+박스 당선작
뷰티/패션 업종의 (주)케이비랩가 크리에잇마켓에서 라벨+박스 디자인을 의뢰한 실제 사례입니다. 총 17개 시안 중 1위작이 선정됐으며, 진행 기간 20일, 의뢰 비용 130만 원, 고객 평점 5점을 기록했습니다.
- 디자인 카테고리
- 라벨+박스 (뷰티/패션 업종)
브랜드 소개
바이오셀룰로오스 시트 마스크팩 파우치 단상자 디자인을 의뢰 합니다.

```html
<!DOCTYPE html>
<html lang="en">
<head>
<meta charset="utf-8">
<title>Venoria Bio Cellulose Mask — Pouch Series</title>
<link href="https://fonts.googleapis.com/css2?family=Work+Sans:wght@300;400;500&display=swap" rel="stylesheet">
<style>
  :root {
    --backdrop: #eeeeea;
    --pouch: #fbfbf9;
    --pouch-edge: #e2e2dd;
    --ink: #2b2b2b;
    --ink-soft: #7a7a78;
    --calming-red: #d8385b;
    --hydrate-blue: #2f72bd;
    --bright-yellow: #e6a93c;
  }
  * { box-sizing: border-box; margin: 0; padding: 0; }
  html, body {
    width: 1200px; height: 1200px; overflow: hidden;
    background: var(--backdrop);
    font-family: "Work Sans", Arial, sans-serif;
    color: var(--ink);
  }
  .canvas { position: relative; width: 1200px; height: 1200px; }

  .pouch {
    position: absolute; top: 375px;
    width: 320px; height: 450px;
    background: var(--pouch);
    border: 1px solid var(--pouch-edge);
    border-radius: 8px;
    box-shadow: 0 10px 28px rgba(0,0,0,0.08);
  }
  .pouch--calming { left: 90px; }
  .pouch--hydrate { left: 440px; }
  .pouch--bright  { left: 790px; }

  .pouch__seal {
    position: absolute; left: 0; right: 0; top: 30px;
    border-top: 1px solid var(--pouch-edge);
  }
  .pouch__notch {
    position: absolute; top: 40px; width: 10px; height: 10px;
    background: var(--backdrop); border-radius: 50%;
  }
  .pouch__notch--left { left: -6px; }
  .pouch__notch--right { right: -6px; }

  .brand {
    position: absolute; left: 28px; top: 56px;
    font-size: 19px; font-weight: 400; line-height: 1.75;
    letter-spacing: 0.02em; color: var(--ink);
  }
  .brand span { display: block; }

  .mark { position: absolute; left: 75px; top: 150px; width: 170px; height: 170px; }

  .variant {
    position: absolute; left: 28px; top: 338px;
    font-size: 11px; font-weight: 500; line-height: 1.35;
  }
  .variant__info {
    display: block; margin-top: 4px;
    font-size: 7px; font-weight: 300; color: var(--ink-soft); line-height: 1.5;
  }
  .weight {
    position: absolute; right: 28px; top: 370px;
    font-size: 12px; font-weight: 500;
  }
  .fine-print {
    position: absolute; left: 28px; right: 28px; top: 400px;
    font-size: 7px; font-weight: 300; color: var(--ink-soft); line-height: 1.55;
  }
</style>
</head>
<body>
<main class="canvas">

  <article class="pouch pouch--calming">
    <div class="pouch__seal"></div>
    <span class="pouch__notch pouch__notch--left"></span>
    <span class="pouch__notch pouch__notch--right"></span>
    <h1 class="brand"><span>Venoria</span><span>Bio</span><span>Cellulose</span></h1>
    <svg class="mark" viewBox="0 0 170 170" aria-hidden="true">
      <polygon points="85,8 165,162 5,162" fill="var(--calming-red)"/>
    </svg>
    <p class="variant">Calming<br>01<span class="variant__info">Bio cellulose sheet<br>1 sheet mask</span></p>
    <p class="weight">27g</p>
    <p class="fine-print">Apply to clean face and rest for twenty minutes before removing.<br>Store in a cool dry place.</p>
  </article>

  <article class="pouch pouch--hydrate">
    <div class="pouch__seal"></div>
    <span class="pouch__notch pouch__notch--left"></span>
    <span class="pouch__notch pouch__notch--right"></span>
    <h2 class="brand"><span>Venoria</span><span>Bio</span><span>Cellulose</span></h2>
    <svg class="mark" viewBox="0 0 170 170" aria-hidden="true">
      <circle cx="85" cy="85" r="82" fill="var(--hydrate-blue)"/>
    </svg>
    <p class="variant">Hydrate<br>02<span class="variant__info">Bio cellulose sheet<br>1 sheet mask</span></p>
    <p class="weight">27g</p>
    <p class="fine-print">Apply to clean face and rest for twenty minutes before removing.<br>Store in a cool dry place.</p>
  </article>

  <article class="pouch pouch--bright">
    <div class="pouch__seal"></div>
    <span class="pouch__notch pouch__notch--left"></span>
    <span class="pouch__notch pouch__notch--right"></span>
    <h2 class="brand"><span>Venoria</span><span>Bio</span><span>Cellulose</span></h2>
    <svg class="mark" viewBox="0 0 170 170" aria-hidden="true">
      <rect x="8" y="8" width="154" height="154" fill="var(--bright-yellow)"/>
    </svg>
    <p class="variant">Bright<br>03<span class="variant__info">Bio cellulose sheet<br>1 sheet mask</span></p>
    <p class="weight">27g</p>
    <p class="fine-print">Apply to clean face and rest for twenty minutes before removing.<br>Store in a cool dry place.</p>
  </article>

</main>
</body>
</html>
```